BKT Business Card

Business card design for a handyman company. Want to portray a professional image and stay away from the "Mom & Pops" image that is normally associated with handyman companies.

```html
<!DOCTYPE html>
<html lang="en">
<head>
<meta charset="utf-8">
<title>BKT Business Card</title>
<link rel="stylesheet" href="https://fonts.googleapis.com/css2?family=Questrial&family=Open+Sans:wght@700&display=swap">
<style>
  :root {
    --backdrop: #8a8588;
    --navy-deep: #0b1c3a;
    --navy-mid: #13305f;
    --navy-text: #0e2244;
    --rule-light: #9fb0c9;
    --white: #ffffff;
    --ink-soft: #2a2a2a;
  }
  html, body {
    margin: 0;
    width: 1200px;
    height: 807px;
    overflow: hidden;
    background: var(--backdrop);
  }
  .card {
    position: absolute;
    left: 122px;
    top: 108px;
    width: 981px;
    height: 609px;
    background: var(--white);
    font-family: "Questrial", sans-serif;
    overflow: hidden;
  }
  .brand-band {
    position: absolute;
    left: 0; top: 0;
    width: 100%; height: 312px;
    background: radial-gradient(ellipse at 50% 45%, var(--navy-mid) 0%, var(--navy-deep) 75%);
  }
  .accent-stripe {
    position: absolute;
    left: 0; top: 316px;
    width: 100%; height: 10px;
    background: var(--navy-deep);
  }
  .footer-band {
    position: absolute;
    left: 0; top: 494px;
    width: 100%; height: 115px;
    background: radial-gradient(ellipse at 50% 30%, var(--navy-mid) 0%, var(--navy-deep) 80%);
  }
  .brand-name {
    position: absolute;
    left: 0; width: 100%;
    top: 58px;
    text-align: center;
    color: var(--white);
    font-size: 96px;
    line-height: 1;
    letter-spacing: 1px;
  }
  .brand-tagline {
    position: absolute;
    left: 0; width: 100%;
    top: 198px;
    text-align: center;
    color: var(--white);
    font-size: 32px;
    letter-spacing: 6px;
    line-height: 1;
  }
  .brand-rule {
    position: absolute;
    left: 211px; top: 249px;
    width: 572px; height: 1px;
    background: var(--rule-light);
  }
  .services {
    position: absolute;
    left: 0; width: 100%;
    top: 256px;
    text-align: center;
    color: var(--white);
    font-family: "Open Sans", sans-serif;
    font-weight: 700;
    font-size: 15px;
    line-height: 20px;
  }
  .holder-name {
    position: absolute;
    left: 26px; top: 344px;
    color: var(--navy-text);
    font-size: 58px;
    line-height: 1;
  }
  .holder-role {
    position: absolute;
    left: 36px; top: 418px;
    color: var(--ink-soft);
    font-size: 22px;
    line-height: 1;
  }
  .contact {
    position: absolute;
    left: 637px; top: 344px;
    color: #111;
    font-size: 23px;
    line-height: 27px;
  }
  .contact p { margin: 0 0 7px; }
  .contact .address { margin: 0; }
  .email {
    position: absolute;
    left: 0; width: 100%;
    top: 558px;
    text-align: center;
    color: var(--white);
    font-size: 26px;
    line-height: 1;
    padding-left: 60px;
    box-sizing: border-box;
  }
</style>
</head>
<body>
  <article class="card">
    <div class="brand-band"></div>
    <div class="accent-stripe"></div>
    <div class="footer-band"></div>

    <div class="brand-name">Brightkeep</div>
    <div class="brand-tagline">Trade Care</div>
    <div class="brand-rule"></div>
    <div class="services">Home Repairs &nbsp;|&nbsp; Handyman Services &nbsp;|&nbsp; Drain Cleaning &nbsp;|&nbsp; Carpet Cleaning</div>

    <div class="holder-name">Dale Morrow</div>
    <div class="holder-role">Proffesional Handyman</div>

    <div class="contact">
      <p>Phone :(555) 014-2271</p>
      <p>Fax: (555) 014-2288</p>
      <p class="address">407 Linden Row<br>Fairview, Ks 60000</p>
    </div>

    <div class="email">info@BrightkeepTrade.com</div>
  </article>
</body>
</html>
```